BRL business card

For a business card with our logo

Contact Information for Business Card

Mathéo VRANEL
Founder & CEO
email : ceo@brightlanterncollective.com / www.brightlanterncollective.com /
instagram / facebook / WhatsApp
N°: +590 690 482 517

Colors

Designer to choose colors to be used in the design.

```html
<!DOCTYPE html>
<html lang="en">
<head>
<meta charset="utf-8">
<title>BRL business card</title>
<link rel="stylesheet" href="https://fonts.googleapis.com/css2?family=Cinzel:wght@500&family=EB+Garamond:wght@400;700&display=swap">
<style>
  :root{
    --stage:#1c1c1e;
    --brand-blue:#0d56a6;
    --brand-orange:#f07a22;
    --card-black:#0e0e0f;
    --ink-light:#e9e9e9;
    --white:#ffffff;
  }
  *{margin:0;padding:0;box-sizing:border-box}
  html,body{width:1200px;height:1200px;overflow:hidden;background:var(--stage)}
  .stage{width:1200px;height:1200px;display:flex;flex-direction:column;align-items:center;justify-content:center;gap:50px}
  .card{width:700px;height:400px;border-radius:22px;position:relative;overflow:hidden;box-shadow:0 18px 40px rgba(0,0,0,.55)}
  .card-front{background:var(--brand-blue);display:flex;align-items:center;justify-content:center}
  .wordmark{display:flex;flex-direction:column;align-items:center;gap:14px;font-family:"Cinzel",serif;font-weight:500;color:var(--white)}
  .wordmark-dot{width:110px;height:110px;border-radius:50%;background:currentColor}
  .wordmark-name{font-size:40px;letter-spacing:1px;line-height:1}
  .wordmark-sub{font-size:18px;letter-spacing:11px;line-height:1}
  .card-back{background:var(--card-black)}
  .back-band{position:absolute;inset:0;width:100%;height:100%}
  .back-logo{position:absolute;left:70px;top:95px;width:300px}
  .back-logo .wordmark{color:var(--brand-blue)}
  .back-logo .wordmark-dot{width:90px;height:90px}
  .back-logo .wordmark-name{font-size:30px}
  .back-logo .wordmark-sub{font-size:15px;letter-spacing:9px}
  .divider{position:absolute;left:392px;top:70px;width:1px;height:170px;background:var(--brand-orange)}
  .contact{position:absolute;left:418px;top:68px;font-family:"EB Garamond",serif;color:var(--ink-light)}
  .person-name{font-weight:700;font-size:30px;line-height:1.1}
  .person-first{color:var(--brand-blue)}
  .person-last{color:var(--brand-orange)}
  .person-role{font-size:17px;margin:2px 0 8px 14px}
  .contact-list{list-style:none;font-size:16px}
  .contact-list li{display:flex;align-items:center;gap:9px;margin:6px 0}
  .contact-list li:first-child{margin-bottom:14px}
  .contact-list .phone-line{margin:0 0 14px 14px}
  .icon{width:18px;height:18px;flex:none}
  .social{position:absolute;display:flex;gap:16px;left:372px;top:305px}
  .social span{width:26px;height:26px;border-radius:50%;border:2px solid var(--white)}
</style>
</head>
<body>
<main class="stage">
  <section class="card card-front" aria-label="Card front">
    <div class="wordmark">
      <span class="wordmark-dot"></span>
      <span class="wordmark-name">BRIGHT LANTERN</span>
      <span class="wordmark-sub">COLLECTIVE</span>
    </div>
  </section>

  <section class="card card-back" aria-label="Card back">
    <svg class="back-band" viewBox="0 0 700 400" preserveAspectRatio="none" aria-hidden="true">
      <path d="M0 400 C180 330 420 250 700 250 L700 400 Z" fill="var(--brand-blue)"/>
    </svg>

    <div class="back-logo">
      <div class="wordmark">
        <span class="wordmark-dot"></span>
        <span class="wordmark-name">BRIGHT LANTERN</span>
        <span class="wordmark-sub">COLLECTIVE</span>
      </div>
    </div>

    <div class="divider"></div>

    <div class="contact">
      <p class="person-name"><span class="person-first">Mathéo</span> <span class="person-last">VRANEL</span></p>
      <p class="person-role">Founder &amp; CEO</p>
      <ul class="contact-list">
        <li>
          <svg class="icon" viewBox="0 0 20 20" aria-hidden="true"><circle cx="10" cy="10" r="10" fill="var(--brand-orange)"/><path d="M7 5.5l2 2-1 1.3a6 6 0 0 0 3.2 3.2l1.3-1 2 2-1.4 1.5C9.5 14.3 5.7 10.5 5.5 7z" fill="var(--card-black)"/></svg>
          +590 690 482 517
        </li>
        <li>
          <svg class="icon" viewBox="0 0 20 20" aria-hidden="true"><circle cx="10" cy="10" r="10" fill="var(--brand-orange)"/><rect x="5" y="6.5" width="10" height="7" fill="none" stroke="var(--card-black)" stroke-width="1.4"/><path d="M5 6.5l5 4 5-4" fill="none" stroke="var(--card-black)" stroke-width="1.4"/></svg>
          ceo@brightlanterncollective.com
        </li>
        <li>
          <svg class="icon" viewBox="0 0 20 20" aria-hidden="true"><circle cx="10" cy="10" r="10" fill="var(--brand-orange)"/><g fill="none" stroke="var(--card-black)" stroke-width="1.2"><circle cx="10" cy="10" r="5"/><ellipse cx="10" cy="10" rx="2.2" ry="5"/><path d="M5 10h10"/></g></svg>
          www.brightlanterncollective.com
        </li>
      </ul>
    </div>

    <div class="social" aria-label="Social channels">
      <span></span><span></span><span></span>
    </div>
  </section>
</main>
</body>
</html>
```